Kestrel Summit 2019 Enemies of the End-Times Church Flyer

We want a church conference flyer designed. We are looking for a professional, yet catchy design that uses our brand colors and logo creatively while communicating key information of the event effectively. <br/>The flyer must include all of the following:<br/>Title: Kestrel Summit 2019<br/>Topic: The Enemies of The End-Times Church <br/>Subtitles: <br/> -How the antichrist raises an army by social behavior engineering. <br/>-How the architects of modern social constructs escaped the church's radar. <br/>-The Holy Spirit's end-times agenda:<br/> The Knock-Out Punch!<br/>Speaker: Prophet Marcus Toliver <br/>Dates/time: December 27, 28 & 29 at 6pm<br/>Location: Halvorn Community Center <br/> 241 Pellham Street <br/> Portland, ME 04102<br/>Contact info: phone: 207-555-0148 <br/>email: contact@brookmeadow.example <br/> www.vutel.example<br/>*The flyer must also include a picture of the speaker and our Vutel logo <br/>Thanks, we look forward to seeing what you come up with!

Colors

Designer to choose colors to be used in the design.

Requirements
Must have
• The flyer must include all of the following:
• Title: Kestrel Summit 2019
• Topic: The Enemies of The End-Times Church
• Subtitles:
• -How the antichrist raises an army by social behavior engineering.
• -How the architects of modern social constructs escaped the church's radar.
• -The Holy Spirit's end-times agenda:
• The Knock-Out Punch!
• Speaker: Prophet Marcus Toliver
• Dates/time: December 27, 28 & 29 at 6pm
• Location: Halvorn Community Center
• 241 Pellham Street
• Portland, ME 04102
• Contact info: phone: 207-555-0148
• email: contact@brookmeadow.example
• www.vutel.example
• *The flyer must also include a picture of the speaker and our Vutel logo
Should not have
• Pictures of crosses or church buildings

```html
<!DOCTYPE html>
<html lang="en">
<head>
<meta charset="utf-8">
<title>Kestrel Summit 2019 Flyer</title>
<link href="https://fonts.googleapis.com/css2?family=Open+Sans:wght@400;600;700;800&family=Roboto+Condensed:wght@400;700&display=swap" rel="stylesheet">
<style>
  :root {
    --navy: #0f3559;
    --sky: #4a8fd6;
    --orange: #ef7d0e;
    --amber: #f39a1f;
    --red: #e23a1f;
    --ink: #1c1c1c;
    --peach: #f8cf9e;
    --cream: #fdf3e8;
    --white: #ffffff;
  }
  * { margin: 0; padding: 0; box-sizing: border-box; }
  html, body { width: 864px; height: 1200px; overflow: hidden; background: var(--white); }
  .flyer { position: relative; width: 864px; height: 1200px; overflow: hidden; font-family: "Open Sans", sans-serif; color: var(--ink); }
  .backdrop { position: absolute; inset: 0; }
  .abs { position: absolute; }
  .brand { right: 0; top: 0; width: 270px; height: 118px; display: flex; align-items: center; justify-content: center; gap: 10px; color: var(--white); }
  .brand-dot { width: 14px; height: 14px; border-radius: 50%; background: var(--orange); }
  .brand-name { font-size: 40px; font-weight: 400; letter-spacing: 2px; }
  .title { left: 0; width: 100%; top: 138px; text-align: center; font-size: 82px; font-weight: 600; color: var(--sky); letter-spacing: -1px; line-height: 1; }
  .year-row { left: 0; width: 100%; top: 240px; display: flex; align-items: center; justify-content: center; gap: 22px; }
  .year-rule { width: 230px; height: 3px; background: var(--amber); }
  .year { font-size: 60px; font-weight: 700; color: var(--amber); line-height: 1; }
  .topic { left: 0; width: 100%; top: 303px; text-align: center; font-size: 32px; font-weight: 400; color: var(--white); letter-spacing: 0.3px; }
  .sessions { left: 54px; top: 568px; width: 460px; list-style: none; }
  .sessions li { position: relative; padding-left: 38px; font-size: 20px; line-height: 29px; color: var(--ink); margin-bottom: 20px; }
  .sessions li::before { content: ""; position: absolute; left: 4px; top: 8px; width: 13px; height: 13px; border-radius: 50%; background: var(--navy); }
  .portrait { left: 555px; top: 486px; width: 198px; height: 198px; border-radius: 50%; background: radial-gradient(circle at 50% 40%, #8a6a4e 0%, #4d3a2c 45%, #c9b9a4 100%); }
  .speaker { left: 614px; top: 770px; font-family: "Roboto Condensed", sans-serif; font-size: 22px; color: var(--ink); }
  .speaker b { color: var(--navy); margin-right: 6px; }
  .pin { left: 411px; top: 818px; }
  .venue { left: 0; width: 100%; top: 850px; text-align: center; font-size: 44px; font-weight: 700; color: var(--orange); letter-spacing: -0.5px; }
  .address { left: 0; width: 100%; top: 906px; text-align: center; font-family: "Roboto Condensed", sans-serif; font-size: 30px; color: var(--navy); }
  .dates { left: 256px; top: 947px; width: 569px; height: 52px; background: var(--navy); color: var(--white); display: flex; align-items: center; justify-content: center; font-size: 30px; font-weight: 700; letter-spacing: -0.3px; }
  .time-row { left: 0; width: 100%; top: 1008px; text-align: center; }
  .time { font-size: 28px; font-weight: 700; color: var(--navy); }
  .time span { color: var(--orange); font-weight: 600; }
  .contact { left: 54px; top: 1072px; color: var(--navy); }
  .contact h3 { font-size: 26px; font-weight: 700; letter-spacing: -0.3px; display: inline-block; border-bottom: 2px solid var(--navy); line-height: 1.2; }
  .contact-line { display: flex; align-items: center; gap: 10px; font-size: 21px; margin-top: 8px; color: var(--navy); }
  .contact-line .item { display: flex; align-items: center; gap: 10px; margin-right: 22px; }
  .icon { width: 22px; height: 22px; flex: none; }
</style>
</head>
<body>
<main class="flyer">
  <svg class="backdrop" width="864" height="1200" viewBox="0 0 864 1200">
    <defs>
      <linearGradient id="sky-glow" x1="0" y1="0" x2="0" y2="1">
        <stop offset="0" stop-color="#c96a1c"/>
        <stop offset="0.22" stop-color="#8c4a22"/>
        <stop offset="0.45" stop-color="#2a2220"/>
        <stop offset="1" stop-color="#161616"/>
      </linearGradient>
      <linearGradient id="lower-field" x1="0" y1="0" x2="1" y2="1">
        <stop offset="0" stop-color="#f7c791"/>
        <stop offset="0.55" stop-color="#fbe6cf"/>
        <stop offset="1" stop-color="#ffffff"/>
      </linearGradient>
    </defs>
    <rect width="864" height="1200" fill="url(#lower-field)"/>
    <g role="img" aria-label="Photograph of a person with raised arms on a hilltop at sunset">
      <path d="M0 0 H864 V440 C800 450 700 470 600 500 C630 470 640 440 610 410 C560 440 500 470 450 470 C410 470 380 420 330 420 C260 420 250 500 160 540 C110 535 50 520 0 515 Z" fill="url(#sky-glow)"/>
    </g>
    <path d="M0 522 C60 525 110 540 160 548 C240 520 270 460 330 428 C300 470 290 510 320 520 C270 530 200 560 160 560 C100 556 50 540 0 538 Z" fill="#141414"/>
    <path d="M600 500 C680 478 760 460 864 450 V462 C770 470 690 490 600 515 Z" fill="#141414"/>
    <path d="M592 0 H864 V118 H650 C615 118 596 96 592 70 Z" fill="var(--navy)"/>
    <rect x="846" y="118" width="18" height="427" fill="var(--navy)"/>
    <circle cx="654" cy="585" r="124" fill="none" stroke="var(--navy)" stroke-width="16" stroke-dasharray="330 800" transform="rotate(150 654 585)"/>
    <circle cx="654" cy="585" r="112" fill="none" stroke="var(--orange)" stroke-width="12"/>
    <path d="M560 660 C600 720 700 740 760 670 C780 640 788 600 782 570 C790 640 750 720 660 728 C610 730 575 700 560 660 Z" fill="var(--red)"/>
    <path d="M0 1200 V1095 C60 1085 110 1070 150 1050 C190 1040 250 1035 300 1045 C230 1060 200 1080 220 1090 C400 1105 600 1100 760 1055 C800 1040 820 1020 864 1010 V1200 Z" fill="var(--orange)"/>
    <line x1="300" y1="1042" x2="700" y2="1042" stroke="var(--navy)" stroke-width="2"/>
  </svg>

  <div class="abs brand"><span class="brand-dot"></span><span class="brand-name">VUTEL</span></div>

  <h1 class="abs title">Kestrel Summit</h1>
  <div class="abs year-row"><span class="year-rule"></span><span class="year">2019</span><span class="year-rule"></span></div>
  <h2 class="abs topic">THE ENEMIES OF THE END-TIMES CHURCH</h2>

  <ul class="abs sessions">
    <li>How the antichrist raises an army by social behavior engineering.</li>
    <li>How the architects of modern social constructs escaped the church's radar.</li>
    <li>The Holy Spirit's end-times agenda.</li>
    <li>The Knock-Out Punch!</li>
  </ul>

  <div class="abs portrait" role="img" aria-label="Photograph of the speaker, Prophet Marcus Toliver"></div>
  <p class="abs speaker"><b>Speaker:</b>Prophet Marcus Toliver</p>

  <svg class="abs pin" width="42" height="46" viewBox="0 0 42 46" aria-hidden="true">
    <ellipse cx="21" cy="38" rx="17" ry="6" fill="none" stroke="var(--ink)" stroke-width="2.5"/>
    <path d="M21 38 C12 27 8 21 8 15 A13 13 0 0 1 34 15 C34 21 30 27 21 38 Z" fill="var(--red)"/>
    <circle cx="21" cy="15" r="5" fill="var(--white)"/>
  </svg>

  <p class="abs venue">Halvorn Community Center</p>
  <p class="abs address">241 Pellham Street, Portland, ME 04102</p>
  <div class="abs dates">DECEMBER 27th 28th AND 29th, 2019</div>
  <p class="abs time-row"><span class="time"><span>TIME:</span> 6pm</span></p>

  <section class="abs contact">
    <h3>Contact info:</h3>
    <div class="contact-line">
      <svg class="icon" viewBox="0 0 22 22" aria-hidden="true"><circle cx="11" cy="11" r="11" fill="var(--navy)"/><path d="M7 5.5 L9 5.5 L10 8.5 L8.6 9.6 C9.3 11 10.8 12.6 12.4 13.4 L13.5 12 L16.5 13 L16.5 15 C16.5 16 15.5 16.6 14.5 16.4 C10 15.6 6.4 12 5.6 7.5 C5.4 6.5 6 5.5 7 5.5 Z" fill="var(--white)"/></svg>
      <span>207-555-0148</span>
    </div>
    <div class="contact-line">
      <span class="item">
        <svg class="icon" viewBox="0 0 22 22" aria-hidden="true"><circle cx="11" cy="11" r="11" fill="var(--navy)"/><rect x="5.5" y="7" width="11" height="8" rx="1" fill="var(--white)"/><path d="M5.5 7.5 L11 11.5 L16.5 7.5" fill="none" stroke="var(--navy)" stroke-width="1.3"/></svg>
        contact@brookmeadow.example
      </span>
      <span class="item">
        <svg class="icon" viewBox="0 0 22 22" aria-hidden="true"><circle cx="11" cy="11" r="11" fill="var(--navy)"/><circle cx="11" cy="11" r="6" fill="none" stroke="var(--white)" stroke-width="1.3"/><ellipse cx="11" cy="11" rx="2.6" ry="6" fill="none" stroke="var(--white)" stroke-width="1.1"/><line x1="5" y1="11" x2="17" y2="11" stroke="var(--white)" stroke-width="1.1"/></svg>
        www.vutel.example
      </span>
    </div>
  </section>
</main>
</body>
</html>
```